Progressive Architecture and Urban Planning Studio - Stationery Design

The Kestrel Collective: a small boutique Architectural and Urban Planning Studio based in Natal/ RN, Brazil, about to open branches in South Africa and West Africa, established to provide high quality, innovative design and personal client service for projects worldwide. Our approach to Architecture: Minimal - Less is More, so to speak, but with an edge! Strive to produce "clean" projects - stripped of all that can be stripped, no excesses. Got our Logo right here with Pixel Harbor, and hope to do the same with our stationery (were informed that includes business cards, letterhead and envelopes). Since we'll be using two clour schemes, we want at least one using a black background (business card). We'll also allow manipulation of our logo if it helps the final design. Good Luck!

Industry/Entity Type

Business

Other font styles liked:
• Nexa

Colors

Designer to choose colors to be used in the design.

Requirements
Must have
• Business Cards/ Letterheads with the following address:
Rua Benedito Sarmento 742, Morro Branco, Natal/RN
Should be able to edit it.

```html
<!DOCTYPE html>
<html lang="en">
<head>
<meta charset="utf-8">
<title>The Kestrel Collective – Business Card</title>
<link rel="stylesheet" href="https://fonts.googleapis.com/css2?family=Montserrat:wght@400;600&family=Arimo:ital,wght@0,400;1,700&display=swap">
<style>
  :root {
    --backdrop: #2b2b2b;
    --card-white: #f4f4f4;
    --card-grey-top: #d2d2d2;
    --card-grey-bottom: #a9a9a9;
    --ink: #1c1c1c;
    --ink-soft: #555555;
    --rule: #8c8c8c;
  }
  * { margin: 0; padding: 0; box-sizing: border-box; }
  html, body { width: 1200px; height: 900px; overflow: hidden; }
  body {
    background: var(--backdrop);
    position: relative;
    font-family: "Arimo", Arial, sans-serif;
    color: var(--ink);
  }
  .card {
    position: absolute;
    width: 540px;
    height: 310px;
    box-shadow: 0 14px 30px rgba(0,0,0,.45);
  }
  .card--back {
    left: 70px; top: 110px;
    background: var(--card-white);
  }
  .card--front {
    left: 590px; top: 470px;
    background: linear-gradient(160deg, var(--card-grey-top), var(--card-grey-bottom));
  }
  .brand {
    font-family: "Montserrat", sans-serif;
    font-weight: 400;
    text-transform: uppercase;
    display: flex;
    align-items: center;
    white-space: nowrap;
  }
  .brand__mark { background: var(--ink); display: inline-block; }
  .card--back .brand {
    position: absolute; left: 250px; top: 48px;
    font-size: 11px; letter-spacing: 4px; color: var(--ink);
  }
  .card--back .brand__mark { width: 14px; height: 14px; margin-right: 10px; }
  .card--front .brand {
    position: absolute; left: 0; right: 0; top: 138px;
    justify-content: center;
    font-size: 21px; letter-spacing: 7px; color: #3a3a3a;
  }
  .card--front .brand__mark { width: 26px; height: 26px; margin-right: 16px; background: #6a6a6a; }
  .person { position: absolute; left: 40px; top: 120px; }
  .person__name { font-size: 19px; color: var(--ink-soft); }
  .person__position { font-size: 11px; font-style: italic; font-weight: 700; color: var(--ink-soft); margin-top: 1px; }
  .divider {
    position: absolute; left: 120px; right: 40px; top: 160px;
    border-top: 1px solid var(--rule);
  }
  .contact { position: absolute; font-size: 10.5px; line-height: 15px; color: var(--ink-soft); }
  .contact--left { left: 40px; top: 176px; }
  .contact--right { left: 330px; top: 176px; }
</style>
</head>
<body>
  <section class="card card--back">
    <div class="brand"><span class="brand__mark"></span>The Kestrel Collective</div>
    <div class="person">
      <p class="person__name">Your Name</p>
      <p class="person__position">Position</p>
    </div>
    <div class="divider"></div>
    <div class="contact contact--left">
      <p>Address: Rua Benedito Sarmento 742,</p>
      <p>Morro Branco, Natal/RN</p>
      <p>Phone: +55 84 3210 4470</p>
    </div>
    <div class="contact contact--right">
      <p>Fax: +55 84 3210 4471</p>
      <p>Email: studio@kestrelcollective.co</p>
      <p>Web: kestrelcollective.co</p>
    </div>
  </section>

  <section class="card card--front">
    <div class="brand"><span class="brand__mark"></span>The Kestrel Collective</div>
  </section>
</body>
</html>
```